lab equipment website

We need a fresh new look for a company website called tarvio. We will be using the current logo and brand colors on their current website tarvio.com. They want to keep their text and on-page SEO, but would like to reformat it to look more modern and fresh. They want to have everything be high performance with a great user experience. Their main call to action is for people to fill in a contact form so they can call them. There is some information that is purposely above the fold on the instrument pages. I will need the home page, about page and a leasing page.

```html
<!DOCTYPE html>
<html lang="en">
<head>
<meta charset="utf-8">
<title>tarvio — Lab equipment service plans and leasing</title>
<link href="https://fonts.googleapis.com/css2?family=PT+Sans:wght@400;700&family=Open+Sans:wght@400;600&display=swap" rel="stylesheet">
<style>
:root{
  --teal:#1fae8c;
  --teal-dark:#145a52;
  --navy:#0f1f5c;
  --blue:#2c4596;
  --blue-soft:#b8c7df;
  --pale:#eaf2fb;
  --text:#3c3f45;
  --muted:#6b7078;
  --white:#ffffff;
}
*{box-sizing:border-box;margin:0;padding:0}
html,body{width:1200px;height:3383px;overflow:hidden}
body{position:relative;font-family:"Open Sans",sans-serif;color:var(--text);background:var(--white)}
h1,h2,h3,h4{font-weight:400}
.btn{position:absolute;display:flex;align-items:center;justify-content:center;background:var(--teal);color:var(--white);font-family:"PT Sans",sans-serif;font-weight:700;font-size:13px;letter-spacing:.5px;border-radius:3px;text-transform:uppercase}

/* hero */
.hero{position:absolute;left:0;top:0;width:1200px;height:614px;background:linear-gradient(180deg,#1e2f6e 0%,#2a3d7f 45%,#1b2a64 100%)}
.brand{position:absolute;left:146px;top:24px;display:flex;align-items:center;gap:10px}
.brand-dot{width:22px;height:22px;border-radius:50%;background:var(--teal)}
.brand-name{font-family:"PT Sans",sans-serif;font-weight:400;font-size:28px;color:var(--white)}
.nav{position:absolute;right:144px;top:28px;display:flex;gap:44px;font-family:"PT Sans",sans-serif;font-size:16px;color:var(--white)}
.nav .active{color:var(--teal)}
.hero-title{position:absolute;left:0;width:1200px;top:254px;text-align:center;font-family:"PT Sans",sans-serif;font-size:40px;color:var(--white)}
.hero-text{position:absolute;left:230px;width:740px;top:310px;text-align:center;font-size:16px;line-height:25px;color:var(--white)}
.dots{position:absolute;left:560px;top:574px;display:flex;gap:6px}
.dots span{width:13px;height:13px;border-radius:50%;border:2px solid var(--white)}
.dots span.on{background:var(--white)}

/* intro */
.intro-title{position:absolute;left:144px;top:686px;width:420px;font-family:"PT Sans",sans-serif;font-size:31px;line-height:40px;color:var(--teal)}
.intro-text{position:absolute;left:144px;top:815px;width:420px;font-size:13px;line-height:24px;color:var(--text)}
.intro-photo{position:absolute;left:629px;top:695px;width:425px;height:327px;background:linear-gradient(135deg,#e4e8ee 0%,#c9cfd8 55%,#2c4aa6 75%,#d4d9e0 100%)}

/* needs */
.needs-photo{position:absolute;left:0;top:1103px;width:600px;height:598px;background:linear-gradient(160deg,#eef2f6 0%,#bfcad6 40%,#2f6ad0 62%,#a9b3bf 100%)}
.needs-panel{position:absolute;left:600px;top:1143px;width:600px;height:601px;background:var(--teal-dark);padding:38px 140px 0 26px;color:#cfe3de}
.needs-panel h2{font-family:"PT Sans",sans-serif;font-size:31px;line-height:40px;color:var(--white);margin-bottom:16px}
.needs-panel p{font-size:12.5px;line-height:23px;color:#a9cdc5}
.needs-panel ul{list-style:none;margin:14px 0 16px}
.needs-panel li{position:relative;padding-left:12px;font-size:12.5px;line-height:19px;color:var(--white);margin-bottom:11px}
.needs-panel li::before{content:"";position:absolute;left:0;top:8px;width:4px;height:4px;border-radius:50%;background:var(--white)}

/* skills */
.group-title{position:absolute;top:1816px;font-family:"PT Sans",sans-serif;font-size:24px;text-align:center}
.skill{position:absolute;top:1870px;width:180px;text-align:center}
.skill svg{display:block;margin:0 auto}
.skill span{display:block;margin-top:10px;font-size:13px;color:var(--muted)}

/* team */
.team{position:absolute;left:0;top:2127px;width:1200px;height:472px;background:var(--pale)}
.team h2{position:absolute;top:70px;width:1200px;text-align:center;font-family:"PT Sans",sans-serif;font-size:31px;color:var(--blue)}
.member{position:absolute;top:132px;width:240px;text-align:center}
.member .name{margin-top:12px;font-family:"PT Sans",sans-serif;font-size:19px;color:#111}
.member .role{font-size:13px;color:var(--muted);margin-top:2px}
.arrow{position:absolute;top:222px}

/* questions */
.ask-title{position:absolute;top:2670px;width:1200px;text-align:center;font-family:"PT Sans",sans-serif;font-size:31px;color:var(--blue)}
.ask-text{position:absolute;top:2722px;width:1200px;text-align:center;font-size:13.5px;color:var(--text)}

/* features */
.features{position:absolute;left:0;top:2879px;width:1200px;height:194px;background:var(--pale)}
.feature{position:absolute;top:46px;width:280px;text-align:center;font-family:"PT Sans",sans-serif;font-size:15.5px;line-height:21px;color:var(--teal)}
.feature svg{display:block;margin:0 auto 10px}

/* footer */
.footer{position:absolute;left:0;top:3073px;width:1200px;height:310px;background:var(--navy);color:var(--white)}
.footer h4{position:absolute;top:52px;font-family:"PT Sans",sans-serif;font-size:16px}
.footer .links{position:absolute;top:82px;font-size:11.5px;line-height:24px;color:#d6dcef}
.footer .contact{position:absolute;left:377px;top:80px;font-size:11px;line-height:15px;color:#d6dcef}
.contact .row{display:flex;gap:10px;margin-bottom:8px}
.newsletter{position:absolute;left:638px;top:83px;width:217px;height:41px;background:#f1f3f8;border-radius:3px;display:flex;align-items:center;justify-content:space-between;padding:0 12px;color:#333;font-size:11px}
.social{position:absolute;left:957px;top:92px;display:flex;gap:22px}
.social span{width:14px;height:14px;border-radius:50%;border:2px solid #c9d1ea}
.footer .rule{position:absolute;left:144px;top:214px;width:912px;height:1px;background:#2b3b78}
.footer .copy{position:absolute;top:258px;width:1200px;text-align:center;font-size:11px;color:#c9d1ea}
</style>
</head>
<body>

<section class="hero" role="img" aria-label="Photo of scientists working in a bright laboratory, tinted deep blue">
  <div class="brand"><span class="brand-dot"></span><span class="brand-name">tarvio</span></div>
  <nav class="nav"><span class="active">HOME</span><span>ABOUT US</span><span>LEASING</span><span>FAQ</span><span>CONTACT US</span></nav>
  <h1 class="hero-title">Our goal is simple: save labs time and money</h1>
  <p class="hero-text">Tarvio is a lab support program that provides scientists with comprehensive maintenance/repair coverage and operating lease solutions at an affordable price.</p>
  <a class="btn" style="left:539px;top:384px;width:122px;height:42px">Read more</a>
  <div class="dots"><span class="on"></span><span></span><span></span><span></span></div>
</section>

<h2 class="intro-title">Trusted Company Offering Scientific Equipment Service Plans and Flexible Leases</h2>
<p class="intro-text">At Tarvio, our goal is to ensure the success of your business. Whether you are running a laboratory or other scientific facilities, we want to keep you provided with the best in cutting-edge equipment. That's why we offer flexible scientific equipment leasing options with worry-free service plans- to provide your business with the tools needed to perform at its peak.</p>
<a class="btn" style="left:144px;top:979px;width:120px;height:43px">Read more</a>
<div class="intro-photo" role="img" aria-label="Photo of a benchtop laboratory instrument with a scientist in the background"></div>

<div class="needs-photo" role="img" aria-label="Photo of a gloved scientist loading sample tubes into a centrifuge"></div>
<section class="needs-panel">
  <h2>We understand your needs<br>because we are scientists first</h2>
  <p>When it comes to creating innovative solutions that cater to your lab, Tarvio's dedicated team of problem-solvers has got you covered. Here's how we save you time and money:</p>
  <ul>
    <li>We collaborate with you directly- no middlemen</li>
    <li>We handle scientific equipment service, repairs, and maintenance</li>
    <li>We consolidate and streamline the ancillary work associated with lab equipment procurement and service</li>
    <li>We utilize our networks to bring you the most cost-savings possible</li>
    <li>We improve cash flow by removing the upfront cost of purchasing, freeing up capital in your everyday budget</li>
    <li>We may provide tax advantages with our lease structures</li>
  </ul>
  <p>We regularly provide businesses with what they need to improve their budget and efficiency. We offer laboratory equipment leasing for a wide range of needs. If you want to discuss your needs more in-depth, don't hesitate to call us at (510) 555-0182 or fill out our contact form.</p>
</section>

<h2 class="group-title" style="left:308px;width:200px;color:var(--teal)">Our Skills</h2>
<h2 class="group-title" style="left:790px;width:200px;color:var(--blue)">The Competition</h2>

<div class="skill" style="left:127px">
  <svg width="146" height="146" viewBox="0 0 146 146"><circle cx="73" cy="73" r="68" fill="none" stroke="var(--teal)" stroke-width="6"/>
  <g fill="none" stroke="var(--teal)" stroke-width="2.5" stroke-linecap="round"><ellipse cx="75" cy="78" rx="24" ry="17"/><path d="M60 92v8M88 92v8M99 76h4M55 68l-5-6"/><circle cx="70" cy="52" r="9"/><path d="M70 47v10"/></g></svg>
  <span>Cost Saving</span>
</div>
<div class="skill" style="left:318px">
  <svg width="146" height="146" viewBox="0 0 146 146"><circle cx="73" cy="73" r="68" fill="none" stroke="var(--teal)" stroke-width="6"/>
  <g fill="none" stroke="var(--teal)" stroke-width="2.5" stroke-linejoin="round"><path d="M52 80l26-26h20v20l-26 26z"/><circle cx="90" cy="62" r="3"/><path d="M66 80l10-10M72 86l8-8"/></g></svg>
  <span>Lease Plan Flexibility</span>
</div>
<div class="skill" style="left:508px">
  <svg width="146" height="146" viewBox="0 0 146 146"><circle cx="73" cy="73" r="68" fill="none" stroke="var(--teal)" stroke-width="6"/>
  <g fill="none" stroke="var(--teal)" stroke-width="2.5" stroke-linejoin="round"><path d="M78 46h26v18H88l-6 6v-6h-4z"/><circle cx="64" cy="70" r="10"/><path d="M46 102c2-14 10-20 18-20s16 6 18 20"/></g></svg>
  <span>Customer Service</span>
</div>
<div class="skill" style="left:700px">
  <svg width="146" height="146" viewBox="0 0 146 146"><circle cx="73" cy="73" r="68" fill="none" stroke="var(--blue-soft)" stroke-width="6"/>
  <circle cx="73" cy="73" r="68" fill="none" stroke="var(--blue)" stroke-width="6" stroke-dasharray="150 427" transform="rotate(-90 73 73)"/>
  <g fill="none" stroke="var(--blue)" stroke-width="2.5" stroke-linejoin="round" stroke-linecap="round"><path d="M73 48l20 7v16c0 13-9 22-20 26-11-4-20-13-20-26V55z"/><path d="M64 73l7 7 12-13"/></g></svg>
  <span>Reliability</span>
</div>
<div class="skill" style="left:891px">
  <svg width="146" height="146" viewBox="0 0 146 146"><circle cx="73" cy="73" r="68" fill="none" stroke="var(--blue-soft)" stroke-width="6"/>
  <circle cx="73" cy="73" r="68" fill="none" stroke="var(--blue)" stroke-width="6" stroke-dasharray="64 427" transform="rotate(-90 73 73)"/>
  <g fill="none" stroke="var(--blue)" stroke-width="2.5"><rect x="48" y="52" width="50" height="44" rx="3"/><path d="M48 62h50M58 46v10M88 46v10"/><circle cx="60" cy="74" r="3"/><circle cx="73" cy="74" r="3"/><circle cx="86" cy="74" r="3"/><circle cx="60" cy="86" r="3"/><circle cx="73" cy="86" r="3"/><circle cx="86" cy="86" r="3"/></g></svg>
  <span>Continued Support</span>
</div>

<section class="team">
  <h2>Our Team</h2>
  <svg class="arrow" style="left:55px" width="16" height="28" viewBox="0 0 16 28"><path d="M14 2L3 14l11 12" fill="none" stroke="#555" stroke-width="2"/></svg>
  <svg class="arrow" style="left:1128px" width="16" height="28" viewBox="0 0 16 28"><path d="M2 2l11 12L2 26" fill="none" stroke="#555" stroke-width="2"/></svg>
  <div class="member" style="left:173px">
    <svg width="240" height="210" viewBox="0 0 240 210"><path d="M136 0l96 96-96 96-96-96z" fill="var(--navy)"/><path d="M120 12l96 96-96 96-96-96z" fill="#c9a88c" role="img" aria-label="Portrait photo of team member"/></svg>
    <div class="name">Marco Lian</div><div class="role">Lab Relations</div>
  </div>
  <div class="member" style="left:480px">
    <svg width="240" height="210" viewBox="0 0 240 210"><path d="M136 0l96 96-96 96-96-96z" fill="var(--navy)"/><path d="M120 12l96 96-96 96-96-96z" fill="#b8a08f" role="img" aria-label="Portrait photo of team member"/></svg>
    <div class="name">Evan Pratt</div><div class="role">Finance</div>
  </div>
  <div class="member" style="left:787px">
    <svg width="240" height="210" viewBox="0 0 240 210"><path d="M136 0l96 96-96 96-96-96z" fill="var(--navy)"/><path d="M120 12l96 96-96 96-96-96z" fill="#9a7a62" role="img" aria-label="Portrait photo of team member"/></svg>
    <div class="name">Ravi Sandhu</div><div class="role">Operations</div>
  </div>
</section>

<h2 class="ask-title">Further questions?</h2>
<p class="ask-text">Feel free to contact us if you have any questions or comments. We promise to get back to you within 24 hours.</p>
<a class="btn" style="left:540px;top:2757px;width:120px;height:41px">Contact us</a>

<section class="features">
  <div class="feature" style="left:150px">
    <svg width="70" height="56" viewBox="0 0 70 56"><g fill="none" stroke="var(--navy)" stroke-width="2.5" stroke-linejoin="round"><rect x="4" y="14" width="62" height="38" rx="3"/><path d="M24 14V6h22v8M4 28h62"/><rect x="29" y="24" width="12" height="9"/></g></svg>
    Worry free lab equipment PM/repair coverage.
  </div>
  <div class="feature" style="left:460px">
    <svg width="70" height="56" viewBox="0 0 70 56"><g fill="none" stroke="var(--navy)" stroke-width="2.5" stroke-linejoin="round"><rect x="16" y="24" width="38" height="30" rx="2"/><path d="M24 24V8M34 24V12M44 24V4M16 38h38"/></g></svg>
    Cost-effective lease structures and<br>payment plans.
  </div>
  <div class="feature" style="left:767px">
    <svg width="70" height="56" viewBox="0 0 70 56"><g fill="none" stroke="var(--navy)" stroke-width="2.5" stroke-linejoin="round"><circle cx="26" cy="16" r="10"/><path d="M8 54c1-16 8-24 18-24s17 8 18 24"/><path d="M52 8h10M54 8v38a3 3 0 006 0V8"/></g></svg>
    Knowledge of the laboratory.
  </div>
</section>

<footer class="footer">
  <h4 style="left:144px">Links</h4>
  <div class="links" style="left:144px">Home<br>About Us<br>Leasing<br>FAQ</div>
  <div class="links" style="left:216px">Contact Us</div>
  <h4 style="left:377px">Contact info</h4>
  <div class="contact">
    <div class="row"><svg width="10" height="13" viewBox="0 0 10 13"><path d="M5 12S1 7 1 5a4 4 0 018 0c0 2-4 7-4 7z" fill="#d6dcef"/></svg><span>220 Harbor Lane, Suite 410<br>Oakdale, CA 94602</span></div>
    <div class="row"><svg width="10" height="12" viewBox="0 0 10 12"><path d="M2 1l2 3-1 1c1 2 2 3 4 4l1-1 2 2-2 2C4 11 0 7 0 3z" fill="#d6dcef"/></svg><span>(510) 555-0182</span></div>
    <div class="row"><svg width="11" height="9" viewBox="0 0 11 9"><rect width="11" height="9" rx="1" fill="#d6dcef"/><path d="M0 1l5.5 4L11 1" fill="none" stroke="var(--navy)"/></svg><span>info@tarvio.com</span></div>
  </div>
  <h4 style="left:636px">Newsletter</h4>
  <div class="newsletter"><span>Email Address</span><svg width="20" height="16" viewBox="0 0 20 16"><path d="M1 7L19 1l-4 14-5-5-3 4V9z" fill="var(--navy)"/></svg></div>
  <h4 style="left:957px">Follow us on</h4>
  <div class="social" aria-label="Social media links"><span></span><span></span><span></span></div>
  <div class="rule"></div>
  <p class="copy">Copyright © 2019 Tarvio. All rights reserved.</p>
</footer>

</body>
</html>
```